Label Design Refresh for existing High End Supplement line

Design a label for our high end supplement brand, packaged in a Cobal Blue bottle.... using Clear labels as the label stock media.

A clear label design will take advantage of the blue bottle and can incorporate any design element you create, metalic elements, new graphics etc.

our line spans 50 different product categories and over 400 unique SKUs, so any elements you suggest to differentiate products or categories will be appreciated.

see: www.velmorahealth.com
Updates

Need designers to meet project requirements. Full label, clear label stock design (clear background with exception for design elements and text etc.)

Target Market(s)

Men and Women 25-55 Health conscious and not price sensitive. Product is 5x higher cost than competition.

Industry/Entity Type

Sexual health for men and women. testosterone, hormone health, nootropics

Font styles to use
Sans Serif

Colors

Designer to choose colors to be used in the design.

Requirements
Must have
• Clear label design for Cobalt blue, packer style, pharma bottle. Must feature Velmora brand on front panel. Must show entire label panel design as 2.8in x 7.25in. Graphics can be full color with metalic or foil type elements.
Nice to have
• Name of products include: SHBG, Testosterone & Libido, Adrenal Support Phase 2, LH Formula, ADHD Phase1,
Should not have
• Busy designs that are stock images for supplement label layouts

```html
<!DOCTYPE html>
<html lang="en">
<head>
<meta charset="utf-8">
<title>Velmora SHBG – Clear Label Panel</title>
<link href="https://fonts.googleapis.com/css2?family=Jost:ital,wght@0,400;0,500;0,600;0,700;0,800;1,400&display=swap" rel="stylesheet">
<style>
  :root {
    --backdrop: #4f5052;
    --label: #6b6c6e;
    --band: #a7a8aa;
    --ink-white: #ffffff;
    --ink-black: #111213;
    --ink-silver: #a3a4a6;
    --accent-green: #8dc63f;
  }
  * { box-sizing: border-box; margin: 0; padding: 0; }
  html, body {
    width: 1200px; height: 900px; overflow: hidden;
    background: var(--backdrop);
    font-family: "Jost", sans-serif;
  }
  .label {
    position: absolute; left: 48px; top: 220px;
    width: 1104px; height: 460px;
    background: var(--label);
    overflow: hidden;
  }
  .pattern-area {
    position: absolute; left: 700px; top: 0; width: 404px; height: 389px;
    background: radial-gradient(ellipse at 65% 45%, rgba(190,200,210,0.28), rgba(190,200,210,0.08) 60%, rgba(107,108,110,0) 85%);
  }
  .info {
    position: absolute; left: 54px; width: 333px;
    color: var(--ink-white); font-size: 14px; line-height: 17px;
    letter-spacing: 0.6px; text-align: justify;
  }
  .info b { font-weight: 500; }
  .directions { top: 36px; }
  .warnings { top: 124px; }
  .fda-box {
    position: absolute; left: 53px; top: 222px; width: 334px; height: 76px;
    border: 1px solid var(--ink-white); border-radius: 5px;
    padding: 6px 10px; color: var(--ink-white);
    font-size: 12px; line-height: 15.5px; letter-spacing: 0.4px; text-transform: uppercase; text-align: justify;
  }
  .brand-small {
    position: absolute; left: 54px; top: 328px;
    color: var(--ink-white); font-weight: 700; font-size: 27px; letter-spacing: -0.5px; text-transform: uppercase;
  }
  .brand-url { position: absolute; left: 54px; top: 364px; color: var(--ink-white); font-size: 13.5px; letter-spacing: 0.3px; }
  .brand-vertical {
    position: absolute; left: 440px; top: 370px; width: 353px;
    transform: rotate(-90deg); transform-origin: 0 0;
    color: var(--ink-black); font-weight: 800; font-size: 68px; line-height: 58px;
    letter-spacing: 0; text-transform: uppercase; white-space: nowrap; text-align: center;
  }
  .brand-dot {
    position: absolute; left: 412px; top: 234px; width: 20px; height: 20px;
    border-radius: 50%; background: var(--accent-green);
  }
  .product-name {
    position: absolute; left: 518px; top: 96px;
    color: var(--ink-silver); font-weight: 600; font-size: 80px; letter-spacing: 7px; line-height: 92px;
  }
  .formula {
    position: absolute; left: 522px; top: 186px;
    color: var(--accent-green); font-weight: 500; font-size: 26px; letter-spacing: 2.4px;
  }
  .benefits {
    position: absolute; left: 528px; top: 268px; list-style: none;
    color: var(--ink-white); font-style: italic; font-size: 17.5px; line-height: 21.7px; letter-spacing: 0.8px;
  }
  .benefits li { display: flex; align-items: center; }
  .benefits li::before {
    content: ""; width: 5px; height: 5px; border-radius: 50%;
    background: var(--ink-white); margin-right: 13px; flex: none;
  }
  .band {
    position: absolute; left: 0; top: 389px; width: 1104px; height: 71px;
    background: var(--band);
  }
  .distributor { position: absolute; left: 54px; top: 8px; width: 258px; color: var(--ink-black); font-size: 11px; line-height: 12.5px; text-align: justify; }
  .distributor b { font-weight: 600; font-size: 12px; display: block; margin-bottom: 2px; }
  .count { position: absolute; left: 522px; top: 2px; color: var(--ink-black); display: flex; align-items: center; gap: 6px; }
  .count-number { font-size: 34px; font-weight: 400; line-height: 44px; }
  .count-text { font-size: 12.5px; line-height: 13px; letter-spacing: 1.2px; text-transform: uppercase; }
  .count-text b { font-weight: 700; letter-spacing: 1.6px; }
  .supplement { position: absolute; left: 522px; top: 45px; color: var(--ink-black); font-size: 14px; letter-spacing: 2.4px; text-transform: uppercase; }
  .band-mark { position: absolute; left: 838px; top: 22px; width: 28px; height: 28px; background: var(--ink-black); }
  .band-name { position: absolute; left: 914px; top: 6px; color: var(--ink-black); font-weight: 700; font-size: 46px; letter-spacing: 4px; line-height: 60px; }
</style>
</head>
<body>
  <section class="label" aria-label="Velmora SHBG clear label panel">
    <div class="pattern-area" role="img" aria-label="Faint silver hexagonal molecular lattice pattern"></div>

    <p class="info directions"><b>DIRECTIONS:</b> Lorem ipsum dolor sit amet, consectetuer adipiscing elit, sed diam nonummy nibh euismod tincidunt ut laoreet dolore magna aliquam erat volutpat.</p>
    <p class="info warnings"><b>WARNINGS:</b> Lorem ipsum dolor sit amet, consectetuer adipiscing elit, sed diam nonummy nibh euismod tincidunt ut laoreet dolore magna aliquam erat volutpat.</p>
    <p class="fda-box">These statements have noot been evaluated by the Food and Drug Administration. This product is not intended to diagnose, treet, cure or prevent any disease.</p>

    <div class="brand-small">Velmora</div>
    <div class="brand-url">www.velmorahealth.com</div>

    <div class="brand-vertical">Velmora</div>
    <div class="brand-dot"></div>

    <h1 class="product-name">SHBG</h1>
    <p class="formula">MENS FORMULA</p>
    <ul class="benefits">
      <li>Testosterone &amp; Libido</li>
      <li>Adrenal Support Phase 2</li>
      <li>LH Formula</li>
      <li>ADHD Phase1</li>
    </ul>

    <div class="band">
      <p class="distributor"><b>Distributed by:</b>Lorem ipsum dolor sit amet, consectetuer adipiscing elit, sed diam nonummy nibh euismod tincidunt ut laoreet</p>
      <div class="count">
        <span class="count-number">60</span>
        <span class="count-text">Vegetable<br><b>Capsules</b></span>
      </div>
      <p class="supplement">Dietary Supplement</p>
      <div class="band-mark"></div>
      <div class="band-name">SHBG</div>
    </div>
  </section>
</body>
</html>
```